Simple, Professional and neat business card design for Vellamor Inc.

We're looking to re-vamp our business card design. We're a supplier of innovative feed ingredients for the North American animal agriculture industry. We are located in Lucknow, Ontario, Canada and our flagship product is a product that prevents milk fever in dairy cows when the calve, it is fed before calving and is very effective compared to other alternatives available on the market today.

Our company has Danish roots and we import all of our product from our Danish partner/manufacturer in Denmark. We like our design to embrace high professionalism while remaining neat and simple.

Target Market(s)

B2B, Feed Mills, Veterinary Clinics, Large integrators/producers,

Industry/Entity Type

Agribusiness

Contact Information for Business Card

We like the rounded corners because they make the card easy to sit in a wallet and not many use it so it makes the card stand out, just possibly something to take account for during the design.

As you can also see on the sliders below, looking for a that simple but proffesional scandinavian design.

Requirements
Nice to have
• Rounded corners
Should not have
• Too vibrant

```html
<!DOCTYPE html>
<html lang="en">
<head>
<meta charset="utf-8">
<title>Vellamor Inc. business cards</title>
<link rel="stylesheet" href="https://fonts.googleapis.com/css2?family=Montserrat:wght@300;400;700&family=Open+Sans:wght@600;700&display=swap">
<style>
  :root {
    --backdrop: #2f3033;
    --navy: #1b4383;
    --navy-deep: #163a74;
    --brand-blue: #1f54a8;
    --ink: #1c1c1c;
    --label-blue: #1f5bb5;
    --gold: #cbb184;
    --white: #ffffff;
  }
  * { box-sizing: border-box; margin: 0; padding: 0; }
  html, body { width: 1200px; height: 1000px; overflow: hidden; }
  body { background: var(--backdrop); position: relative; font-family: "Open Sans", Arial, sans-serif; }

  .card {
    position: absolute;
    width: 760px;
    height: 420px;
    border-radius: 34px;
    box-shadow: 0 18px 40px rgba(0,0,0,0.45);
  }

  /* Front */
  .card-front {
    left: 320px; top: 50px;
    background: linear-gradient(160deg, var(--brand-blue) 0%, var(--navy) 55%, var(--navy-deep) 100%);
    display: flex; flex-direction: column; align-items: center; justify-content: center;
    color: var(--white);
  }
  .front-mark {
    width: 120px; height: 120px; border-radius: 50%;
    background: var(--gold); margin-bottom: 26px;
  }
  .front-name {
    font-family: "Montserrat", Arial, sans-serif;
    font-weight: 700; font-size: 46px; letter-spacing: 0.5px;
  }
  .front-tagline {
    font-family: "Montserrat", Arial, sans-serif;
    font-weight: 300; font-size: 24px; margin-top: 6px;
  }

  /* Back */
  .card-back {
    left: 120px; top: 530px;
    background: var(--white);
    padding: 42px 0 0 70px;
    color: var(--ink);
  }
  .person-name { color: var(--navy); font-weight: 700; font-size: 25px; margin-bottom: 18px; }
  .address { font-weight: 600; font-size: 16px; line-height: 1.3; margin-bottom: 14px; }
  .contact-list { list-style: none; font-weight: 600; font-size: 17px; line-height: 1.3; }
  .contact-label { color: var(--label-blue); }
  .web-lines { font-weight: 600; font-size: 17px; line-height: 1.3; margin-top: 8px; }
  .web-lines .accent { color: var(--label-blue); }

  .social-row { display: flex; gap: 20px; margin-top: 16px; }
  .social-dot { width: 30px; height: 30px; border-radius: 50%; background: var(--gold); }

  .back-brand {
    position: absolute; right: 50px; bottom: 34px;
    display: flex; align-items: center; gap: 18px;
  }
  .back-brand-mark { width: 58px; height: 58px; border-radius: 50%; background: var(--gold); }
  .back-brand-name {
    font-family: "Montserrat", Arial, sans-serif;
    font-weight: 700; font-size: 38px; color: var(--brand-blue);
  }
</style>
</head>
<body>
  <section class="card card-front">
    <div class="front-mark"></div>
    <div class="front-name">VELLAMOR INC.</div>
    <div class="front-tagline">Caring for the wellbeing of every herd</div>
  </section>

  <section class="card card-back">
    <h1 class="person-name">Anders Holmgaard</h1>
    <p class="address">Box 412, Eldermoor, Westvale<br>Canada K7R4M2</p>
    <ul class="contact-list">
      <li><span class="contact-label">Mobile:</span> 555-214-0147</li>
      <li><span class="contact-label">Office:</span> 555-214-0182</li>
      <li><span class="contact-label">Toll Free:</span> 800-555-0129</li>
      <li><span class="contact-label">Fax:</span> 555-214-0163</li>
    </ul>
    <p class="web-lines">anders@vellamor.com<br>www.<span class="accent">vellamor</span>.com</p>
    <div class="social-row">
      <span class="social-dot"></span>
      <span class="social-dot"></span>
      <span class="social-dot"></span>
    </div>
    <div class="back-brand">
      <span class="back-brand-mark"></span>
      <span class="back-brand-name">VELLAMOR INC.</span>
    </div>
  </section>
</body>
</html>
```